Math Help Website Needs New Design

Looking to refresh the design of my existing site (quillnumberdesk.com) to be easier on the eyes. I am fully capable of doing the HTML coding and have for years, but I don't have the eye for good design, colors, layout, and fonts. This is where I need help!

I need both a new design scheme and a new logo that matches. The overall functionality will be the same as the existing site, and should not be unrecognizable.

Target Market(s)

It should appeal to students (age 13-22) and their parents, so it should NOT be childish in appearance, nor should it be corporate.

Requirements
Must have
• Should be simple, easy-to-navigate, and neither childish nor corporate. I am looking for a design for both the homepage and a similar "content" page. Simple, bold colors are preferred. A logo should be prominent at the top, with a search bar nearby. Below that I need a similar navigational area like I already have. Then, I need about 200px wide ad space on the left of the main body area.

```html
<!DOCTYPE html>
<html lang="en">
<head>
<meta charset="utf-8">
<title>Quill Number Desk – Math Help</title>
<link href="https://fonts.googleapis.com/css2?family=Montserrat:wght@400;600;700&family=Open+Sans:wght@400;600;700&display=swap" rel="stylesheet">
<style>
:root{
  --sky-top:#d9f3fb;
  --sky-mid:#3fc4ec;
  --sky-deep:#14a9e0;
  --green:#3f9a2c;
  --green-light:#6cbf3a;
  --green-dark:#2e7d20;
  --cyan:#1bb6e8;
  --orange:#f08a0c;
  --orange-deep:#e26a06;
  --ink:#2f2f2f;
  --muted:#8a8a8a;
  --link:#19a7de;
  --rust:#c8430e;
  --paper:#ffffff;
  --line:#dcdcdc;
  --pale-yellow:#fde08d;
  --grey-panel:#ececec;
}
*{margin:0;padding:0;box-sizing:border-box}
html,body{width:768px;height:1200px;overflow:hidden}
body{
  position:relative;
  font-family:"Open Sans",Arial,sans-serif;
  color:var(--ink);
  background:linear-gradient(180deg,var(--sky-top) 0px,#8ddcf4 180px,var(--sky-mid) 520px,var(--sky-deep) 1200px);
}
.abs{position:absolute}
/* header */
.brand{left:77px;top:18px;font-family:"Montserrat",sans-serif;font-weight:700;font-size:22px;color:var(--green);display:flex;align-items:center;gap:8px;white-space:nowrap}
.brand-dot{width:11px;height:11px;border-radius:50%;background:var(--green)}
.online-pill{left:347px;top:21px;width:197px;height:20px;border-radius:10px;background:#3a3a3a;color:#fff;font-size:7.6px;line-height:20px;padding-left:10px;white-space:nowrap;overflow:hidden}
.search{left:554px;top:21px;width:135px;height:20px;border-radius:10px;background:#f3f7f8;border:1px solid #cfe3ea;font-size:8px;color:#9aa;line-height:18px;padding-left:12px}
.nav{left:77px;top:60px;width:614px;height:33px;border-radius:4px 4px 0 0;background:linear-gradient(180deg,var(--green-light),var(--green));display:flex;align-items:center;justify-content:space-between;padding:0 6px}
.nav a{font-family:"Montserrat",sans-serif;font-weight:700;font-size:10px;color:#fff;text-decoration:none;padding:4px 9px;border-radius:11px;white-space:nowrap}
.nav a.current{background:#fff;color:var(--green)}
.page{left:77px;top:93px;width:614px;height:1015px;background:var(--paper)}
/* hero */
.hero{left:88px;top:104px;width:590px;height:212px;border:1px solid var(--line);background:linear-gradient(90deg,#fff 0,#f4f8fa 100%);overflow:hidden}
.hero h1{position:absolute;left:27px;top:22px;font-family:"Montserrat",sans-serif;font-weight:600;font-size:27px;line-height:32px;color:#333;letter-spacing:-.5px;white-space:nowrap}
.hero h1 span{color:var(--green-light)}
.hero p{position:absolute;left:27px;top:94px;width:250px;font-size:8.5px;line-height:13px;color:#333}
.cta{position:absolute;left:27px;top:152px;width:170px;height:26px;background:linear-gradient(180deg,#8ccf3c,var(--green));clip-path:polygon(0 0,92% 0,100% 50%,92% 100%,0 100%);color:#fff;font-family:"Montserrat",sans-serif;font-weight:700;font-size:11px;line-height:26px;padding-left:12px;display:flex;align-items:center;gap:6px}
.hero-photo{position:absolute;left:320px;top:0;width:270px;height:212px;border-radius:120px 0 0 120px;background:linear-gradient(120deg,#3c4a4a,#6b7a74 45%,#c9a58a 75%,#e3cfb8)}
/* ad */
.ad{left:88px;top:340px;width:153px;height:155px;border:1px solid var(--line);background:#fff}
.ad-badge{position:absolute;left:16px;top:16px;width:120px;height:120px;border:1px solid #b9c77a;background:#f5f8ec;display:flex;align-items:center;justify-content:center;text-align:center;font-family:"Montserrat",sans-serif;font-weight:700;font-size:12px;color:#2a6f8a;padding:8px;line-height:16px}
/* feature tiles */
.tile{top:340px;width:209px;height:143px;color:#fff;padding:14px 16px}
.tile h2{font-family:"Montserrat",sans-serif;font-weight:600;font-size:15px;margin-bottom:6px}
.tile li{list-style:none;font-size:9.5px;line-height:14.5px;display:flex;gap:5px;align-items:center;white-space:nowrap}
.tile .btn{position:absolute;bottom:12px;left:16px;width:108px;height:13px;border-radius:7px;background:#e9eef0;color:#777;font-size:7px;font-weight:700;text-align:center;line-height:13px}
.tile-new{left:252px;background:linear-gradient(135deg,#28c6f0,#0aa6de)}
.tile-lessons{left:470px;background:linear-gradient(135deg,#f9a21a,var(--orange-deep))}
.tile-art{position:absolute;right:10px;top:30px;width:66px;height:80px;border-radius:6px;background:rgba(255,255,255,.12)}
/* study group */
.study{left:88px;top:496px;width:153px;height:313px;background:var(--green)}
.study h3{height:30px;display:flex;align-items:center;gap:8px;padding-left:10px;font-family:"Montserrat",sans-serif;font-weight:600;font-size:12px;color:#fff;border-bottom:1px solid rgba(255,255,255,.25)}
.study-icon{width:18px;height:18px;border-radius:50%;background:#fff}
.post{display:flex;gap:8px;padding:9px 10px;border-bottom:1px solid rgba(255,255,255,.25);font-size:8.5px;line-height:11.5px;color:#fff}
.avatar{flex:none;width:22px;height:22px;background:#e9efe6;border:1px solid #fff}
.ask{left:88px;top:809px;width:153px;height:121px;background:var(--grey-panel);padding:10px}
.ask h3{font-family:"Montserrat",sans-serif;font-weight:600;font-size:12px;color:#444;margin-bottom:4px}
.ask p{width:86px;font-size:8px;line-height:11px;color:#555}
.ask-photo{position:absolute;right:4px;bottom:12px;width:44px;height:72px;border-radius:22px 22px 4px 4px;background:linear-gradient(180deg,#d9b48f,#79b95a)}
/* discussions */
.section-title{left:252px;top:509px;font-family:"Montserrat",sans-serif;font-weight:600;font-size:16px;color:#333}
.disc{left:252px;top:533px;width:426px;height:161px;border:1px solid var(--line);border-radius:3px}
.disc-photo{position:absolute;left:7px;top:7px;width:146px;height:146px;background:linear-gradient(135deg,#4a5553,#8a8f7e 55%,#7d4fa0)}
.topic{position:absolute;left:161px;width:255px}
.topic b{display:block;color:var(--link);font-size:8.5px;font-weight:700}
.topic span{display:block;font-size:8.5px;color:#444;white-space:nowrap}
.topic i{display:block;font-style:normal;font-size:7px;color:var(--muted)}
.more-btn{position:absolute;right:12px;bottom:6px;width:108px;height:14px;border-radius:7px;background:#e8edef;color:var(--link);font-size:7px;font-weight:700;text-align:center;line-height:14px}
/* solver */
.tabs{left:252px;top:712px;width:426px;height:20px;border-bottom:2px solid var(--rust);display:flex;font-size:9px;color:#333;white-space:nowrap}
.tabs span{padding:3px 7px}
.tabs .on{background:var(--rust);color:#fff}
.toolbar{left:252px;top:748px;width:426px;display:flex;justify-content:space-between}
.tool{width:18px;height:18px;background:#e3dde0;border:1px solid #c9bfc4;position:relative}
.tool::after{content:"";position:absolute;left:4px;top:6px;width:8px;height:4px;border:1px solid #8a4e6a}
.shapes{left:252px;top:778px}
.label{left:257px;font-size:8.5px;font-weight:700;color:#333;white-space:nowrap}
.problem{left:347px;top:817px;width:326px;height:39px;background:var(--pale-yellow);font-size:8.5px;color:#8a7a4a;padding:13px 12px}
.examples{left:347px;top:861px;width:326px;height:116px;background:#f1f1f1;border:1px solid #d8d8d8;padding:14px 18px;font-size:8.5px;line-height:17px;color:#888}
.arrow-btn{left:346px;width:80px;height:21px;background:var(--rust);clip-path:polygon(0 0,86% 0,100% 50%,86% 100%,0 100%);color:#fff;font-size:8.5px;font-weight:700;line-height:21px;padding-left:10px;white-space:nowrap}
.select{left:347px;top:1017px;width:326px;height:25px;background:#efefef;border:1px solid #d6d6d6}
.select svg{position:absolute;right:6px;top:7px}
/* footer */
.footer{left:0;width:768px;text-align:center;color:#fff;font-size:8.5px;white-space:nowrap}
</style>
</head>
<body>
<div class="abs brand"><span>Quill Number Desk</span><span class="brand-dot"></span></div>
<div class="abs online-pill">57 People online They can help you right now</div>
<div class="abs search">Search</div>

<nav class="abs nav">
  <a>HOME</a><a class="current">ALGEBRA</a><a>GEOMETRY</a><a>TRIG</a><a>CALCULUS</a><a>STATISTICS</a><a>MORE SUBJECTS</a><a>MESSAGE BOARD</a>
</nav>

<div class="abs page"></div>

<section class="abs hero">
  <h1>Welcome to<br><span>Quill Number</span> Desk</h1>
  <p>Math Lessons - Looking to understand a subject better, or maybe you don't understand what your textbook is trying to tell you? We have a collection of algebra and geometry lessons that you can view online right now.</p>
  <div class="cta"><svg width="12" height="10" viewBox="0 0 12 10"><path d="M1 5l3.5 3.5L11 1.5" stroke="#fff" stroke-width="2.2" fill="none"/></svg>GET STARTED NOW</div>
  <div class="hero-photo" role="img" aria-label="Smiling student holding a pencil in front of a chalkboard"></div>
</section>

<aside class="abs ad">
  <div class="ad-badge">Brightpath Study Guides</div>
</aside>

<section class="abs tile tile-new">
  <h2>What's New?</h2>
  <ul>
    <li>✔ Multiplying Polynomials</li>
    <li>✔ Derivative of an Inverse Function</li>
    <li>✔ Derivatives of Logs and Exps</li>
    <li>✔ Differentiating Trig Functions</li>
  </ul>
  <div class="btn">MORE MATH LESSONS</div>
</section>
<section class="abs tile tile-lessons">
  <h2>Math Lessons</h2>
  <ul>
    <li>✔ Algebra</li><li>✔ Geometry</li><li>✔ Trigonometry</li><li>✔ Calculus</li><li>✔ Statistics</li>
  </ul>
  <div class="tile-art" role="img" aria-label="Illustration of geometry tools and numbers"></div>
  <div class="btn">MORE MATH LESSONS</div>
</section>

<section class="abs study">
  <h3><span class="study-icon"></span>Live Study Group</h3>
  <div class="post"><span class="avatar"></span><span>At the half-time show, a marching band marched in formation. The lead drummer started at a point with coordinates (-2, -5) and moved 3 steps...</span></div>
  <div class="post"><span class="avatar"></span><span>Write the direct variation equation for the following: y varies directly with x and y = 60 when x = 10</span></div>
  <div class="post"><span class="avatar"></span><span>how do I do this question? see attached</span></div>
  <div class="post"><span class="avatar"></span><span>Comput.e the discriminant of the quadratic equation</span></div>
</section>
<section class="abs ask">
  <h3>Ask Your Question</h3>
  <p>On our math help message board. Just be sure to explain what you've tried to do and where you're stuck, and a friendly volunteer may try to assist you!</p>
  <div class="ask-photo" role="img" aria-label="Student pointing toward the question panel"></div>
</section>

<h2 class="abs section-title">Current Discussions</h2>
<section class="abs disc">
  <div class="disc-photo" role="img" aria-label="Teacher holding papers beside a chalkboard of equations"></div>
  <div class="topic" style="top:10px"><b>Help!! Metric Units</b><span>I don't getany of this. all I know is that a kilometer is 1000...</span><i>Posted by: MarkT</i></div>
  <div class="topic" style="top:51px"><b>Calculating percentile and standard d...</b><span>I don't getany of this. all I know is that a kilometer is 1000...</span><i>Posted by: ProfLee</i></div>
  <div class="topic" style="top:92px"><b>Linear word problem</b><span>I need help solving this: In order to obtain maximum...</span><i>Posted by: MarkT</i></div>
  <div class="more-btn">MORE MATH LESSONS</div>
</section>

<div class="abs tabs"><span>Basic Math</span><span class="on">Pre-Algebra</span><span>Algebra</span><span>Trigonometry</span><span style="margin-left:14px">Precalculus</span><span style="margin-left:6px">Calculus</span><span>Statistics</span></div>
<div class="abs toolbar">
  <span class="tool"></span><span class="tool"></span><span class="tool"></span><span class="tool"></span><span class="tool"></span><span class="tool"></span><span class="tool"></span><span class="tool"></span><span class="tool"></span><span class="tool"></span><span class="tool"></span><span class="tool"></span>
</div>
<svg class="abs shapes" width="426" height="20" viewBox="0 0 426 20" fill="none" stroke="#8a4e6a" stroke-width="1.2">
  <rect x="2" y="3" width="14" height="14"/>
  <circle cx="47" cy="10" r="7"/>
  <path d="M73 17l8-14 8 14z"/>
  <path d="M108 17l4-13h14l-4 13z"/>
  <path d="M143 17l3-12h10l3 12z"/>
  <path d="M180 7h10v10h-10zM180 7l4-4h10l-4 4M194 3v10l-4 4"/>
  <ellipse cx="221" cy="5" rx="6" ry="2"/><path d="M215 5v11a6 2 0 0 0 12 0V5"/>
  <path d="M254 3l-7 13a7 2 0 0 0 14 0z"/>
  <path d="M287 3l-8 14h14zM287 3l6 14"/>
  <circle cx="322" cy="10" r="7"/><ellipse cx="322" cy="10" rx="7" ry="2"/>
  <text x="347" y="15" font-size="13" fill="#8a4e6a" stroke="none">÷</text>
  <text x="382" y="15" font-size="12" fill="#8a4e6a" stroke="none">π</text>
</svg>

<div class="abs label" style="top:818px">Enter Problem:</div>
<div class="abs problem">enter your problem here.....</div>
<div class="abs label" style="top:862px">Examples:</div>
<div class="abs examples">
  Expand , Variables, Expressions, and Integers<br>
  Simplifying and Evaluating Expressions<br>
  Solving Equations<br>
  Multi-Step Equations and Inequalities<br>
  Factors, Fractions, and Exponents
</div>
<div class="abs label" style="top:986px">Math Format</div>
<div class="abs arrow-btn" style="top:985px">Show Result</div>
<div class="abs label" style="top:1024px">Select Topic</div>
<div class="abs select"><svg width="7" height="10" viewBox="0 0 7 10"><path d="M1 4l2.5-3 2.5 3M1 6l2.5 3 2.5-3" stroke="#999" fill="none"/></svg></div>
<div class="abs arrow-btn" style="top:1051px">Find Answer</div>

<div class="abs footer" style="top:1128px">Home &nbsp;|&nbsp; Algebra &nbsp;|&nbsp; Geometry &nbsp;|&nbsp; Trig &nbsp;|&nbsp; Calculus &nbsp;|&nbsp; Statistics &nbsp;|&nbsp; More Subjects &nbsp;|&nbsp; Message Board</div>
<div class="abs footer" style="top:1143px">All Right Reserved Copyright © 2013 - Privacy Policy &nbsp;|&nbsp; Terms</div>
<div class="abs footer" style="top:1158px;font-size:7.5px">Powered By Northlane Studio</div>
</body>
</html>
```